Ferncrest Dental, LLC business card project

Business card to be designed with current logo.
Dental office- please keep design of card that looks clean and professional.
Please include the following info:
Ferncrest Dental, LLC
Dr. Lorna Pettigrew
2871 Marlowe Street
Havenbrook, VT 05999
610-555-0193
ferncrestdental.office@examplemail.test
Hello everyone-
Reason: Just got back from overseas- will look at all designs and provide feedback. Thank you!
Reason: Polling my friends for the final selection-
thank you to all those that participated- so many talented designers!

```html
<!DOCTYPE html>
<html lang="en">
<head>
<meta charset="utf-8">
<title>Ferncrest Dental, LLC — Business Card</title>
<link rel="stylesheet" href="https://fonts.googleapis.com/css2?family=Arimo:wght@400;700&family=Share+Tech+Mono&display=swap">
<style>
  :root {
    --backdrop: #e6e6e3;
    --leaf-green: #62a53c;
    --lime: #a5c93a;
    --paper: #fbfbf8;
    --ink: #161616;
    --icon-blue: #3d7fc1;
    --shadow: rgba(0, 0, 0, 0.18);
  }
  * { box-sizing: border-box; margin: 0; padding: 0; }
  html, body {
    width: 1200px;
    height: 900px;
    overflow: hidden;
    background: var(--backdrop);
  }
  .canvas {
    position: relative;
    width: 1200px;
    height: 900px;
  }
  .card {
    position: absolute;
    left: 250px;
    width: 700px;
    height: 400px;
    border-radius: 4px 22px 4px 4px;
    overflow: hidden;
    background: var(--paper);
    box-shadow: 0 10px 28px var(--shadow);
  }
  .card--front { top: 35px; }
  .card--back { top: 465px; }
  .card__art {
    position: absolute;
    inset: 0;
    width: 100%;
    height: 100%;
  }
  .brand-name {
    position: absolute;
    right: 34px;
    bottom: 40px;
    font-family: "Arimo", sans-serif;
    font-weight: 400;
    font-size: 38px;
    line-height: 1;
    color: var(--leaf-green);
    letter-spacing: 0.5px;
    white-space: nowrap;
  }
  .doctor-name {
    position: absolute;
    left: 70px;
    top: 96px;
    font-family: "Arimo", sans-serif;
    font-weight: 700;
    font-size: 29px;
    line-height: 1;
    color: var(--ink);
    white-space: nowrap;
  }
  .contact {
    position: absolute;
    right: 28px;
    top: 236px;
    list-style: none;
    font-family: "Share Tech Mono", monospace;
    color: var(--ink);
    text-transform: uppercase;
  }
  .contact__line {
    display: flex;
    align-items: center;
    justify-content: flex-end;
    gap: 10px;
    font-size: 20px;
    letter-spacing: 2.5px;
    line-height: 26px;
    white-space: nowrap;
  }
  .contact__line--email {
    font-size: 13px;
    letter-spacing: 1.2px;
    margin-top: 2px;
  }
  .contact__icon {
    width: 18px;
    height: 18px;
    flex: none;
  }
  .contact__icon--blank { visibility: hidden; }
</style>
</head>
<body>
<main class="canvas">

  <section class="card card--front" aria-label="Card front">
    <svg class="card__art" viewBox="0 0 700 400" aria-hidden="true">
      <rect width="700" height="400" fill="var(--leaf-green)"/>
      <path d="M0 352 C180 300 420 250 700 222 L700 400 L0 400 Z" fill="var(--lime)"/>
      <path d="M0 374 C200 330 440 280 700 256 L700 400 L0 400 Z" fill="var(--paper)"/>
    </svg>
    <p class="brand-name">Ferncrest Dental, LLC</p>
  </section>

  <section class="card card--back" aria-label="Card back">
    <svg class="card__art" viewBox="0 0 700 400" aria-hidden="true">
      <rect width="700" height="400" fill="var(--paper)"/>
      <ellipse cx="90" cy="100" rx="360" ry="230" fill="var(--lime)"/>
      <path d="M0 358 C220 352 460 366 700 400 L0 400 Z" fill="var(--lime)"/>
    </svg>

    <h1 class="doctor-name">Dr. Lorna Pettigrew</h1>

    <ul class="contact">
      <li class="contact__line">610-555-0193
        <svg class="contact__icon" viewBox="0 0 18 18" aria-hidden="true"><path d="M4 2 L7 2 L8 6 L6 7.5 C7 10 8 11 10.5 12 L12 10 L16 11 L16 14 C16 15 15 16 14 16 C8 16 2 10 2 4 C2 3 3 2 4 2 Z" fill="var(--icon-blue)"/></svg>
      </li>
      <li class="contact__line">2871 Marlowe Street
        <svg class="contact__icon" viewBox="0 0 18 18" aria-hidden="true"><path d="M9 1 C5.5 1 3 3.6 3 7 C3 11 9 17 9 17 C9 17 15 11 15 7 C15 3.6 12.5 1 9 1 Z" fill="var(--icon-blue)"/><circle cx="9" cy="7" r="2.3" fill="var(--paper)"/></svg>
      </li>
      <li class="contact__line">Havenbrook, VT 05999
        <svg class="contact__icon contact__icon--blank" viewBox="0 0 18 18" aria-hidden="true"></svg>
      </li>
      <li class="contact__line contact__line--email">ferncrestdental.office@examplemail.test
        <svg class="contact__icon" viewBox="0 0 18 18" aria-hidden="true"><rect x="1.5" y="4" width="15" height="10" rx="1.5" fill="var(--icon-blue)"/><path d="M2.5 5 L9 10 L15.5 5" stroke="var(--paper)" stroke-width="1.4" fill="none"/></svg>
      </li>
    </ul>
  </section>

</main>
</body>
</html>
```